'Cradle Ahead' promotional brochure

We have designed a 6 week program to educate impending first-time parents about the things they need to know to survive the first 6 months. Sessions delivered by general practitioner/family doctor, dietician, physiotherapist, speech pathologist and psychologist. Our promotional blurb is: 'A comprehensive education program for first-time parents-to-be, delivered over 6 weeks by health professionals in your community, about everything you need to know to look after your baby (and yourself!) in the first 6 months'. I now want to put together a promotional brochure to be distributed to those couples who express an interest which will provide further details of what will be delivered in the course.
Updates
In terms of layout, I envisaged a double sided A4 size, foldable into 3 sections, but very happy to be guided on this.
Target Market(s)
To appeal to a young, well educated demographic. First time parents couples.
Industry/Entity Type
Medical
Font styles to use
Other font styles liked:
- Playfair Display
Requirements
Must have
- Playfair display font to be consistent with our logo (attached). Logo also included please. Some consistency with colours of logo please.
Nice to have
- I am a doctor, and have no creative genes! But prefer a clean and professional appearance overall. Not too cluttered in overall appearance.
Should not have
- No cheesy pictures of babies.

```html
<!DOCTYPE html>
<html lang="en">
<head>
<meta charset="utf-8">
<title>Cradle Ahead – Brochure</title>
<link href="https://fonts.googleapis.com/css2?family=Playfair+Display:wght@400&family=Raleway:wght@300;400&display=swap" rel="stylesheet">
<style>
:root{
  --bg:#d5d6d8;
  --green:#6dbd45;
  --green-dark:#4f9a2e;
  --grey:#787878;
  --grey-mid:#8a8a8a;
  --paper:#ffffff;
  --text:#5d5d5d;
  --serif:'Playfair Display', Georgia, serif;
  --sans:'Raleway', Arial, sans-serif;
}
*{box-sizing:border-box;margin:0;padding:0}
html,body{width:892px;height:1200px;overflow:hidden;background:var(--bg)}
body{position:relative;font-family:var(--sans);color:var(--text)}
h1,h2,h3{font-weight:400}
.spread{position:absolute;left:98px;width:676px;height:477px;box-shadow:0 12px 10px -8px rgba(0,0,0,.35);overflow:hidden;background:var(--paper)}
.spread--outside{top:99px}
.spread--inside{top:633px}
.panel{position:absolute;top:0;height:100%;overflow:hidden}
.panel--1{left:0;width:225px}
.panel--2{left:225px;width:226px}
.panel--3{left:451px;width:225px}
.fold-shade{background:linear-gradient(90deg,rgba(0,0,0,.06),rgba(0,0,0,0) 20%,rgba(0,0,0,0) 80%,rgba(0,0,0,.06))}
.layer{position:absolute;inset:0}
.brand{position:absolute;display:flex;align-items:center;gap:9px}
.brand__mark{width:22px;height:22px;background:var(--green)}
.brand__name{font-family:var(--serif);color:var(--green);font-size:13px;line-height:1.05;text-transform:uppercase;letter-spacing:.5px}
.title{font-family:var(--serif);color:var(--green);text-transform:uppercase;letter-spacing:.5px}
.serif-copy{font-family:var(--serif);text-align:center}
/* outside left */
.cover-left .title{position:absolute;top:154px;width:100%;text-align:center;font-size:23px}
.cover-left .lead{position:absolute;top:204px;width:100%;font-size:9.5px;color:#222;line-height:1.35;text-transform:uppercase}
.cover-left .note{position:absolute;width:100%;font-size:10px;color:#666;line-height:1.3}
.cover-left .price{position:absolute;top:300px;width:100%;font-size:10px;color:var(--green-dark);text-transform:uppercase}
/* contact */
.contact{background:var(--grey);color:#fff}
.contact__head{position:absolute;top:41px;width:100%;font-family:var(--serif);font-size:12.5px;line-height:1.3;text-align:center;text-transform:uppercase}
.contact__rule{position:absolute;top:78px;left:34px;width:157px;border-top:1px dotted rgba(255,255,255,.5)}
.contact__org{position:absolute;top:92px;width:100%;font-family:var(--serif);font-size:9px;line-height:1.4;text-align:center;text-transform:uppercase}
.contact__addr{position:absolute;top:127px;width:100%;font-size:8px;line-height:1.45;text-align:center}
.contact__phone{position:absolute;top:173px;width:100%;font-size:9.5px;text-align:center}
.contact__mail{position:absolute;top:199px;width:100%;font-size:7.5px;text-align:center}
.contact__web{position:absolute;top:446px;width:100%;font-size:8.5px;text-align:center}
/* outside right */
.cover-right .title--white{position:absolute;top:424px;width:100%;text-align:center;font-size:24px;color:#fff}
/* inside */
.band{position:absolute;top:0;left:0;width:100%;height:115px;background:var(--grey)}
.inside-title{position:absolute;top:55px;width:100%;text-align:center;font-family:var(--serif);font-size:27px;color:#e4e4e4;text-transform:uppercase;letter-spacing:.5px}
.week{position:absolute;font-size:6.8px;line-height:1.45;color:var(--text)}
.week h3{font-family:var(--serif);font-size:11.5px;color:var(--green);text-transform:uppercase;padding-bottom:3px;margin-bottom:7px;border-bottom:1px dotted #cfcfcf;width:170px}
.week p{text-align:justify;margin-bottom:6px}
.week .session{color:var(--green)}
.week ul{list-style:none}
.week li{position:relative;padding-left:7px;margin-bottom:1.5px;white-space:nowrap}
.week li::before{content:"";position:absolute;left:0;top:3px;width:3.5px;height:3.5px;border-radius:50%;background:#bdbdbd}
.cols{display:flex}
.cols ul:first-child{width:83px}
.cols ul:last-child{flex:1}
.week--p1{left:18px;right:11px}
.week--p2{left:19px;right:11px}
.week--p3{left:15px;right:14px}
</style>
</head>
<body>

<section class="spread spread--outside">
  <div class="panel panel--1 cover-left fold-shade">
    <svg class="layer" width="225" height="477" viewBox="0 0 225 477">
      <defs><linearGradient id="handsFill" x1="0" y1="0" x2="1" y2="1"><stop offset="0" stop-color="#cfcfcf"/><stop offset="1" stop-color="#9c9c9c"/></linearGradient></defs>
      <path d="M0 408 C60 372 140 356 225 356 L225 477 L0 477 Z" fill="var(--green)"/>
      <path d="M0 418 C60 382 140 366 225 364 L225 477 L0 477 Z" fill="url(#handsFill)" role="img" aria-label="Black and white photo of parents' hands cradling a newborn's feet"/>
    </svg>
    <div class="brand" style="left:42px;top:56px">
      <div class="brand__mark"></div>
      <div class="brand__name">Tallowood<br>Health &amp;<br>Medical</div>
    </div>
    <h1 class="title" style="top:128px">Cradle Ahead</h1>
    <p class="lead serif-copy" style="top:166px">A comprehensive education<br>program for first-time parents.</p>
    <p class="note serif-copy" style="top:201px">Delivered over 6 weeks by health<br>professionals in your community.</p>
    <p class="note serif-copy" style="top:239px">Everything you need to know to look after<br>Your baby (and yourself!)<br>In the first 6 months</p>
    <p class="price serif-copy">Total cost $300</p>
  </div>

  <div class="panel panel--2 contact">
    <svg class="layer" width="226" height="477" viewBox="0 0 226 477">
      <circle cx="90" cy="-12" r="70" fill="none" stroke="rgba(255,255,255,.3)"/>
      <circle cx="113" cy="309" r="88" fill="none" stroke="rgba(255,255,255,.25)"/>
      <circle cx="113" cy="309" r="78" fill="var(--grey-mid)"/>
      <circle cx="113" cy="309" r="65" fill="#e8e8e8" role="img" aria-label="Street map showing the clinic location"/>
      <path d="M126 284 a7 7 0 0 1 7 7 c0 6 -7 13 -7 13 s-7 -7 -7 -13 a7 7 0 0 1 7 -7z" fill="#555"/>
      <circle cx="126" cy="291" r="2.5" fill="#e8e8e8"/>
      <path d="M0 356 C70 380 150 410 226 386 L226 477 L0 477 Z" fill="var(--green)"/>
      <path d="M0 356 C70 380 150 410 226 386" fill="none" stroke="var(--grey-mid)" stroke-width="2"/>
    </svg>
    <h2 class="contact__head">Contact details for<br>enquiries bookings</h2>
    <div class="contact__rule"></div>
    <p class="contact__org">Tallowood<br>Health &amp; Medical</p>
    <p class="contact__addr">Tallowood Plaza, Shop 7<br>215 Banksia Parade<br>Tallowood NSW 2999</p>
    <p class="contact__phone">02 5550 0142</p>
    <p class="contact__mail">hello@tallowoodhealth.example</p>
    <p class="contact__web">www.tallowoodhealth.example</p>
  </div>

  <div class="panel panel--3 cover-right">
    <svg class="layer" width="225" height="477" viewBox="0 0 225 477">
      <defs><linearGradient id="familyFill" x1="0" y1="0" x2="1" y2="1"><stop offset="0" stop-color="#5a5a5a"/><stop offset=".5" stop-color="#9a9a9a"/><stop offset="1" stop-color="#3e3e3e"/></linearGradient></defs>
      <path d="M0 112 C80 118 170 98 225 70 L225 477 L0 477 Z" fill="var(--green)"/>
      <path d="M0 122 C80 126 170 110 225 86 L225 477 L0 477 Z" fill="#a6a6a6"/>
      <path d="M0 128 C80 132 170 118 225 96 L225 390 C160 396 80 400 0 400 Z" fill="url(#familyFill)" role="img" aria-label="Black and white photo of a mother and father holding their newborn"/>
      <path d="M0 398 C90 398 170 388 225 372 L225 477 L0 477 Z" fill="var(--green)"/>
    </svg>
    <div class="brand" style="left:34px;top:40px">
      <div class="brand__mark" style="width:28px;height:28px"></div>
      <div class="brand__name" style="font-size:16px">Tallowood<br>Health &amp;<br>Medical</div>
    </div>
    <h1 class="title title--white">Cradle Ahead</h1>
  </div>
</section>

<section class="spread spread--inside">
  <div class="panel panel--1 fold-shade">
    <svg class="layer" width="225" height="477" viewBox="0 0 225 477">
      <defs><linearGradient id="feetFill" x1="0" y1="0" x2="1" y2="1"><stop offset="0" stop-color="#bdbdbd"/><stop offset="1" stop-color="#e6e6e6"/></linearGradient></defs>
      <rect x="0" y="0" width="225" height="115" fill="var(--grey)"/>
      <circle cx="64" cy="48" r="100" fill="var(--green)"/>
      <circle cx="56" cy="42" r="96" fill="#fff"/>
      <circle cx="56" cy="42" r="92" fill="url(#feetFill)" role="img" aria-label="Black and white close-up photo of a newborn's feet"/>
    </svg>
    <div class="week week--p1" style="top:160px">
      <h3>Week 1</h3>
      <p style="text-align:left">GP Dr Hannah Whitcombe will share information for Mum's own health after delivery. Topics include:</p>
      <ul>
        <li>Vaccinations in pregnancy</li>
        <li>Bleeding, bladder and bowel after delivery</li>
        <li>Breastfeeding, engorgement and mastitis</li>
        <li>Bottle feeding</li>
        <li>Post-natal anxiety &amp; depression</li>
        <li>Intimacy and contraception</li>
      </ul>
    </div>
    <div class="week week--p1" style="top:298px">
      <h3>Week 2</h3>
      <p><span class="session">Session 1</span> – Clinical Psychologist Dr Maren Ashby will discuss changes in relationships as couples becomes parents, gender roles in parenting and post-natal depression.</p>
      <p><span class="session">Session 2</span> – Physiotherapist Tessa Holloway will present advice for Mums regarding exercise during and after pregnancy, looking after the pelvic floor during and after pregnancy, and abdominal muscle separation management. She will also provide advice for promoting babies' neck strength and minimising the risk of flat spots on the head and encouraging gross motor skills in the first 6 months</p>
    </div>
  </div>

  <div class="panel panel--2 fold-shade">
    <div class="band"></div>
    <svg class="layer" width="226" height="477" viewBox="0 0 226 477">
      <circle cx="85" cy="125" r="95" fill="none" stroke="rgba(255,255,255,.35)"/>
      <ellipse cx="113" cy="432" rx="62" ry="44" fill="#e6e6e6" role="img" aria-label="Black and white photo of a smiling baby under a towel"/>
    </svg>
    <h2 class="inside-title">Cradle Ahead</h2>
    <div class="week week--p2" style="top:160px">
      <h3>Week 3</h3>
      <p><span class="session">Session 1</span> – Dietician Nina Garrick provides advice for Mums regarding healthy eating during pregnancy and lactation, normal weight gain during pregnancy and realistic weight loss after. She will also discuss the evidence regarding breastfeeding VS bottle-feeding, normal infant weight gain and introducing solids (including those with potential for allergy).</p>
      <p><span class="session">Session 2</span> – Paediatric Speech Pathologist Ruth Calder will share information about latching and breast-feeding troubles &amp; tongue tie, advice about dummies and finger-sucking, introducing solids &amp; feeding (including 'pouch' food), encouraging language development and current evidence about electronic devices impacting language development. strength and minimising the risk of flat spots on the head and encouraging gross motor skills in the first 6 months</p>
    </div>
  </div>

  <div class="panel panel--3 fold-shade">
    <div class="band"></div>
    <svg class="layer" width="225" height="477" viewBox="0 0 225 477">
      <circle cx="140" cy="140" r="95" fill="none" stroke="rgba(255,255,255,.35)"/>
    </svg>
    <div class="week week--p3" style="top:160px">
      <h3>Week 4</h3>
      <p style="text-align:left">GP Dr Hannah Whitcombe will share advice about your babies' health in the first 6 months, including:</p>
      <div class="cols">
        <ul><li>Skin of newborns</li><li>Sleeping</li><li>Crying</li><li>Immunisations</li></ul>
        <ul><li>Fever and infections</li><li>Diarrhoea and constipation</li><li>Teething</li><li>Understanding a baby's signals</li></ul>
      </div>
    </div>
    <div class="week week--p3" style="top:273px">
      <h3>Week 5</h3>
      <p><span class="session">Session 1</span> – Clinical Psychologist Dr Maren Ashby will share information about bonding &amp; attachment with your baby, how to promote their social &amp; emotional development and how to manage separation anxiety. She will also discuss positive parenting approaches.</p>
    </div>
    <div class="week week--p3" style="top:358px">
      <h3>Week 6</h3>
      <p><span class="session">Session 1</span> – Secret Men's Business – a men-only session (including beer!) with a new father for frank discussion about the road ahead. Mums will do a shopping excursion with the GP &amp; Dietician to Greenbay Grocers to look at baby products and food – the good and the bad!</p>
      <p><span class="session">Session 2</span> – Program review, reflection and evaluation and future session planning when baby is 6 months of age.</p>
    </div>
  </div>
</section>

</body>
</html>
```